Flyer, Anzeige & Aufkleber für Massagen gestalten
Zielgruppe
Massage. Gaymassage. Wellness. Kosmetik
Aufgabenstellung
Anfertigung eines Flyers, Anzeige und Aufkleber ....

```html
<!DOCTYPE html>
<html lang="de">
<head>
<meta charset="utf-8">
<title>Massage for Men in Munich – Flyer</title>
<link rel="stylesheet" href="https://fonts.googleapis.com/css2?family=Cabin:wght@600;700&family=Marcellus&family=Tenor+Sans&display=swap">
<style>
  :root {
    --orange: #f26a10;
    --grey-text: #5e5e5e;
    --white: #ffffff;
    --wall: #8e5f4c;
    --wall-dark: #6a4234;
    --skin: #d9a184;
    --skin-light: #ecc6b0;
    --towel: #f3f0ee;
  }
  html, body {
    margin: 0;
    padding: 0;
    width: 800px;
    height: 1200px;
    overflow: hidden;
    background: var(--white);
  }
  .flyer {
    position: relative;
    width: 800px;
    height: 1200px;
    overflow: hidden;
    background: var(--white);
  }
  .hero-photo {
    position: absolute;
    left: 0;
    top: 0;
    width: 800px;
    height: 840px;
    background: linear-gradient(172deg,
      var(--wall) 0%,
      var(--wall) 22%,
      var(--wall-dark) 36%,
      var(--skin) 48%,
      var(--skin-light) 60%,
      var(--skin) 68%,
      #e9dfda 76%,
      var(--towel) 86%,
      #f7f7f7 100%);
  }
  .title {
    position: absolute;
    left: 193px;
    top: 30px;
    width: 400px;
    margin: 0;
    color: var(--white);
    font-family: "Marcellus", serif;
    font-weight: 400;
    text-align: center;
    text-shadow: 2px 3px 4px rgba(0,0,0,0.55);
  }
  .title-main {
    display: block;
    font-size: 90px;
    line-height: 84px;
  }
  .title-rule {
    height: 3px;
    background: var(--white);
    box-shadow: 1px 2px 3px rgba(0,0,0,0.4);
    margin: 2px 0 0;
  }
  .title-sub {
    display: block;
    font-size: 45px;
    line-height: 58px;
  }
  .title-city {
    display: block;
    font-size: 74px;
    line-height: 72px;
    margin-top: 4px;
  }
  .badge {
    position: absolute;
    left: 503px;
    top: 572px;
    width: 224px;
    height: 224px;
    border-radius: 50%;
    box-sizing: border-box;
    border: 7px solid var(--orange);
    background: radial-gradient(circle at 40% 35%, #fafafa 0%, #e6e6e6 70%, #d8d8d8 100%);
    box-shadow: 2px 4px 8px rgba(0,0,0,0.3);
  }
  .badge-text {
    position: absolute;
    left: 0;
    top: 42px;
    width: 100%;
    text-align: center;
    color: var(--orange);
    font-family: "Marcellus", serif;
    font-size: 64px;
    line-height: 60px;
    -webkit-text-stroke: 1px var(--orange);
    transform: rotate(-15deg);
  }
  .badge-rule {
    display: block;
    width: 160px;
    height: 3px;
    margin: 0 auto;
    background: var(--orange);
  }
  .services {
    position: absolute;
    left: 0;
    top: 848px;
    width: 800px;
    margin: 0;
    text-align: center;
    color: var(--grey-text);
    font-family: "Cabin", sans-serif;
    font-weight: 700;
    font-size: 40px;
    line-height: 55px;
  }
  .services-row { display: block; white-space: nowrap; }
  .sep { margin: 0 14px; }
  .hotline {
    position: absolute;
    left: 0;
    top: 980px;
    width: 800px;
    text-align: center;
    color: var(--orange);
    font-family: "Cabin", sans-serif;
    font-weight: 600;
    font-size: 73px;
    line-height: 84px;
    text-shadow: 1px 2px 2px rgba(0,0,0,0.2);
    white-space: nowrap;
  }
  .website {
    position: absolute;
    left: 0;
    top: 1066px;
    width: 800px;
    text-align: center;
    color: var(--grey-text);
    font-family: "Tenor Sans", sans-serif;
    font-size: 46px;
    line-height: 54px;
  }
  .contact-line {
    position: absolute;
    left: 0;
    top: 1138px;
    width: 800px;
    text-align: center;
    color: var(--orange);
    font-family: "Cabin", sans-serif;
    font-weight: 700;
    font-size: 28px;
    line-height: 34px;
    white-space: nowrap;
  }
</style>
</head>
<body>
  <div class="flyer">
    <div class="hero-photo" role="img" aria-label="Photo: a man lying face down on a white massage towel with hot stones on his back, candles in a warm brown spa room behind him"></div>

    <h1 class="title">
      <span class="title-main">MASSAGE</span>
      <div class="title-rule"></div>
      <span class="title-sub">FOR MEN BY MAN</span>
      <div class="title-rule"></div>
      <span class="title-city">IN MUNICH</span>
    </h1>

    <div class="badge">
      <div class="badge-text">OPEN<span class="badge-rule"></span>DAILY</div>
    </div>

    <p class="services">
      <span class="services-row">Seifenschaum<span class="sep">|</span>Ganzkörper<span class="sep">|</span>Wellness</span>
      <span class="services-row">Rücken<span class="sep">|</span>Intimrasur<span class="sep">|</span>Po Relax<span class="sep">|</span>Tantra</span>
    </p>

    <div class="hotline">Hotline 0152/384 19 07</div>
    <div class="website">www.pfefferhain72.com</div>
    <div class="contact-line">Lindenhof 14 | München 80331 &nbsp;| info@pfefferhain72.com</div>
  </div>
</body>
</html>
```